QRN Law Letterhead

Want law firm letterhead - both in terms of a pdf file that I can use electronically as letterhead by adding it as a background - and in terms of a file that I can send to a company to create actual letterhead.
Industry/Entity Type
Law Firm
Font styles to use
Sans Serif
Requirements
Must have
- Should have the following information (you can decide where to place):
- My name - Emil Vostrakian
- My email - emil@qrnlegalgroup.example
- My address - 2861 Corvella Parkway 318-742
- San Jose, California 95342
- Website - www.qrnlegalgroup.example
- Phone - 408-297-1586
- Fax - 408-853-2941
- The logo I attached
Nice to have
- I think I would prefer to have a black and white color scheme.
- I don't necessarily need a title after my name, but I have seen a few design submissions that include a generic title. The title I would use is "IP Litigator & Trademark Attorney"

```html
<!DOCTYPE html>
<html lang="en">
<head>
<meta charset="utf-8">
<title>QRN Law Letterhead</title>
<link href="https://fonts.googleapis.com/css2?family=Open+Sans:wght@400;600;700&display=swap" rel="stylesheet">
<style>
  :root {
    --backdrop: #e2e3e1;
    --paper: #ffffff;
    --slate: #3f5d71;
    --slate-light: #5f7b8c;
    --ink: #1f1c1d;
    --ink-soft: #5b5859;
    --text: #231f20;
    --muted: #4a4a4a;
  }
  * { margin: 0; padding: 0; box-sizing: border-box; }
  html, body {
    width: 1200px; height: 784px; overflow: hidden;
    background: var(--backdrop);
    font-family: "Open Sans", Arial, sans-serif;
  }
  .canvas {
    position: relative; width: 1200px; height: 784px;
    display: flex; align-items: center; justify-content: center;
  }
  .letterhead {
    position: relative; width: 572px; height: 740px;
    background: var(--paper);
    box-shadow: 0 2px 10px rgba(0,0,0,0.12);
    overflow: hidden;
  }
  .letterhead__art { position: absolute; inset: 0; width: 100%; height: 100%; }
  .brand-mark {
    position: absolute; left: 22px; top: 16px;
    display: flex; align-items: center; gap: 6px;
    color: #fff; font-weight: 700; font-size: 13px; letter-spacing: 1px;
  }
  .brand-mark__dot {
    width: 16px; height: 16px; border-radius: 50%;
    border: 2px solid #fff;
  }
  .identity {
    position: absolute; left: 40px; top: 92px; width: 210px;
    text-align: right; color: var(--text);
  }
  .identity__firm { font-size: 27px; font-weight: 600; color: var(--ink); line-height: 1; letter-spacing: -0.5px; }
  .identity__name { font-size: 10.5px; font-weight: 600; color: var(--slate); margin-top: 4px; }
  .identity__title { font-size: 8.5px; color: var(--muted); margin-top: 1px; }
  .contact {
    position: absolute; right: 24px; top: 118px; width: 250px;
    text-align: right; font-size: 7.5px; color: var(--muted); line-height: 1.6;
  }
  .contact__heading {
    display: flex; align-items: center; gap: 8px;
    font-size: 8.5px; font-weight: 700; color: var(--slate);
  }
  .contact__heading::before, .contact__heading::after {
    content: ""; flex: 1; height: 1px; background: #b7c2c9;
  }
  .contact__address { font-weight: 700; color: var(--slate); }
  .contact__row { display: flex; justify-content: flex-end; gap: 10px; }
  .contact__item { display: inline-flex; align-items: center; gap: 3px; }
  .contact__icon { width: 7px; height: 7px; fill: var(--slate); }
</style>
</head>
<body>
<main class="canvas">
  <section class="letterhead">
    <svg class="letterhead__art" viewBox="0 0 572 740" preserveAspectRatio="none" aria-hidden="true">
      <defs>
        <linearGradient id="slateBand" x1="0" y1="0" x2="1" y2="0">
          <stop offset="0" stop-color="var(--slate)"/>
          <stop offset="1" stop-color="var(--slate-light)"/>
        </linearGradient>
        <linearGradient id="inkSwoop" x1="0" y1="1" x2="1" y2="0">
          <stop offset="0" stop-color="var(--ink)"/>
          <stop offset="0.6" stop-color="#2b2829"/>
          <stop offset="1" stop-color="var(--ink-soft)"/>
        </linearGradient>
      </defs>
      <path class="band-top" d="M0 0 H572 V6 C470 20 330 44 200 62 C110 74 40 92 0 118 Z" fill="url(#slateBand)"/>
      <path class="swoop-bottom" d="M200 740 C330 724 470 690 572 585 V740 Z" fill="url(#inkSwoop)"/>
    </svg>

    <div class="brand-mark">
      <span class="brand-mark__dot"></span>
      <span>QRN</span>
    </div>

    <header class="identity">
      <h1 class="identity__firm">QRN Law</h1>
      <p class="identity__name">Emil Vostrakian</p>
      <p class="identity__title">IP Litigator &amp; Trademark Attorney</p>
    </header>

    <address class="contact" style="font-style:normal">
      <div class="contact__heading">QRN Law</div>
      <div class="contact__address">2861 Corvella Parkway 318-742 San Jose, California 95342</div>
      <div class="contact__row">
        <span class="contact__item">
          <svg class="contact__icon" viewBox="0 0 10 10"><path d="M2 0.5 L3.6 0.5 L4.3 3 L3.2 3.8 C3.8 5.2 4.8 6.2 6.2 6.8 L7 5.7 L9.5 6.4 V8 C9.5 9 8.7 9.5 8 9.5 C3.8 9.2 0.8 6.2 0.5 2 C0.5 1.3 1 0.5 2 0.5 Z"/></svg>
          408-297-1586
        </span>
        <span class="contact__item">
          <svg class="contact__icon" viewBox="0 0 10 10"><rect x="2" y="0.5" width="6" height="3"/><rect x="0.5" y="4" width="9" height="4" rx="1"/><rect x="2" y="7" width="6" height="2.5"/></svg>
          408-853-2941
        </span>
      </div>
      <div class="contact__row">
        <span class="contact__item">
          <svg class="contact__icon" viewBox="0 0 10 10"><rect x="0.5" y="2" width="9" height="6" rx="1"/></svg>
          emil@qrnlegalgroup.example
        </span>
        <span class="contact__item">
          <svg class="contact__icon" viewBox="0 0 10 10"><circle cx="5" cy="5" r="4.5"/></svg>
          www.qrnlegalgroup.example
        </span>
      </div>
    </address>
  </section>
</main>
</body>
</html>
```